New business card for my lawn and landscape business

Hollin Yard and Building is a full-service lawn care, landscaping, and light construction company serving Paragould and the Northeast Arkansas region. The business is owned and operated by Dorian Waltham, with a reputation for hands-on, detail-oriented service, dependable crews, and quality results for both residential and commercial clients. A well regarded business with great reviews.
Owner Dorian Waltham
Hollinyardandbuilding.example

Target Market(s)

Commercial, Middle, and upper class in north east Arkansas

Industry/Entity Type

Lawn maintenance and landscape

Contact Information for Business Card

Hollin Yard And Building Professional lawn care, landscaping, and property improvement in Northeast Arkansas. • lawn maintenance •lawn treatments and weed control • exterior projects • Custom landscape design & installation • Sod, trees, rock & drainage solutions • Residential & commercial services Reliable. Detailed. Done right.

Requirements
Must have
• Business name, service area, list of some of our services, clean design that represents
Nice to have
• Unique. Different design element than just grass because its already in n the logo. Picture of a warm season (south) lawn or landscape. Pictures of the type of work we do

```html
<!DOCTYPE html>
<html lang="en">
<head>
<meta charset="utf-8">
<title>Hollin Yard and Building – Business Card</title>
<link href="https://fonts.googleapis.com/css2?family=Poppins:wght@400;500;600;700&family=Roboto:wght@400;500&display=swap" rel="stylesheet">
<style>
  :root{
    --stage:#2b2b2e;
    --card:#262629;
    --panel:#3a3a3e;
    --green:#6cbf3c;
    --green-deep:#3f7d22;
    --text-light:#d9d9db;
    --text-white:#f4f4f4;
  }
  *{margin:0;padding:0;box-sizing:border-box}
  html,body{width:1200px;height:952px;overflow:hidden;background:var(--stage)}
  body{position:relative;font-family:"Poppins",sans-serif}

  .card{
    position:absolute;width:560px;height:320px;background:var(--card);
    overflow:hidden;border-radius:3px;box-shadow:0 14px 30px rgba(0,0,0,.45);
  }
  .card--front{left:320px;top:120px}
  .card--back{left:320px;top:512px}

  .brand{
    position:absolute;display:flex;align-items:center;gap:10px;
    color:var(--green);font-weight:600;font-size:17px;letter-spacing:.5px;
    text-transform:uppercase;line-height:1.1;
  }
  .brand__dot{width:34px;height:34px;border-radius:50%;border:3px solid var(--green);flex:none}
  .card--front .brand{left:36px;top:34px}
  .card--back .brand{right:40px;top:34px}

  .service-area{
    position:absolute;right:40px;top:82px;
    font-family:"Roboto",sans-serif;font-size:12px;color:var(--text-light);letter-spacing:.3px;
  }

  .contact{position:absolute;right:40px;top:112px;text-align:right}
  .contact__name{color:var(--green);font-weight:600;font-size:25px;letter-spacing:.6px;text-transform:uppercase;line-height:1.3}
  .contact__role{color:var(--text-light);font-size:15px;margin-top:2px;margin-bottom:12px}
  .contact__line{display:flex;justify-content:flex-end;align-items:center;gap:8px;color:var(--text-light);font-size:13px;line-height:1.75}
  .contact__line svg{width:14px;height:14px;flex:none}
  .contact__line--plain{padding-right:22px}

  .services{position:absolute;list-style:none;font-family:"Roboto",sans-serif;font-size:12.5px;color:var(--text-white)}
  .services li{display:flex;align-items:center;gap:7px;line-height:1.95}
  .services svg{width:13px;height:13px;flex:none}
  .services--left{left:36px;top:40px}
  .services--right{right:40px;top:132px}

  .turf-band{
    position:absolute;left:0;bottom:0;width:100%;height:46px;
    background:linear-gradient(180deg,var(--green) 0%,var(--green-deep) 100%);
  }
</style>
</head>
<body>

<section class="card card--front">
  <div class="brand"><span class="brand__dot"></span><span>Hollin Yard<br>and Building</span></div>

  <div class="contact">
    <h1 class="contact__name">Dorian Waltham</h1>
    <p class="contact__role">Owner &amp; Managing Director</p>
    <p class="contact__line">+1 870 555 0142
      <svg viewBox="0 0 16 16"><path fill="var(--green)" d="M4 1l3 3-1.6 2a9 9 0 0 0 4.6 4.6L12 9l3 3-2 3C7 15 1 9 1 3z"/></svg></p>
    <p class="contact__line contact__line--plain">info@hollinyard.example</p>
    <p class="contact__line">office@hollinyard.example
      <svg viewBox="0 0 16 16"><rect x="1" y="3" width="14" height="10" fill="var(--green)"/><path d="M1 3l7 6 7-6" stroke="var(--card)" stroke-width="1.4" fill="none"/></svg></p>
    <p class="contact__line">www.hollinyardandbuilding.example
      <svg viewBox="0 0 16 16"><circle cx="8" cy="8" r="7" fill="none" stroke="var(--green)" stroke-width="1.6"/><path d="M1 8h14M8 1c-3 4-3 10 0 14M8 1c3 4 3 10 0 14" stroke="var(--green)" stroke-width="1.2" fill="none"/></svg></p>
  </div>
</section>

<section class="card card--back">
  <ul class="services services--left">
    <li><svg viewBox="0 0 14 14"><rect x=".5" y=".5" width="13" height="13" fill="none" stroke="#fff"/><path d="M3 7l3 3 5-7" stroke="var(--green)" stroke-width="2" fill="none"/></svg>Lawn Maintenance</li>
    <li><svg viewBox="0 0 14 14"><rect x=".5" y=".5" width="13" height="13" fill="none" stroke="#fff"/><path d="M3 7l3 3 5-7" stroke="var(--green)" stroke-width="2" fill="none"/></svg>Lawn Treatments And Weed Control</li>
    <li><svg viewBox="0 0 14 14"><rect x=".5" y=".5" width="13" height="13" fill="none" stroke="#fff"/><path d="M3 7l3 3 5-7" stroke="var(--green)" stroke-width="2" fill="none"/></svg>Exterior Projects</li>
  </ul>

  <div class="brand"><span class="brand__dot"></span><span>Hollin Yard<br>and Building</span></div>
  <p class="service-area">Serving Paragould &amp; Northeast Arkansas</p>

  <ul class="services services--right">
    <li><svg viewBox="0 0 14 14"><rect x=".5" y=".5" width="13" height="13" fill="none" stroke="#fff"/><path d="M3 7l3 3 5-7" stroke="var(--green)" stroke-width="2" fill="none"/></svg>Custom Landscape Design &amp; Installation</li>
    <li><svg viewBox="0 0 14 14"><rect x=".5" y=".5" width="13" height="13" fill="none" stroke="#fff"/><path d="M3 7l3 3 5-7" stroke="var(--green)" stroke-width="2" fill="none"/></svg>Sod, Trees, Rock &amp; Drainage Solutions</li>
    <li><svg viewBox="0 0 14 14"><rect x=".5" y=".5" width="13" height="13" fill="none" stroke="#fff"/><path d="M3 7l3 3 5-7" stroke="var(--green)" stroke-width="2" fill="none"/></svg>Residential &amp; Commercial Services Reliable</li>
  </ul>

  <div class="turf-band" role="img" aria-label="Illustrated strip of green grass blades along the bottom edge"></div>
</section>

</body>
</html>
```